Marketing Business Card Design

I am, launching a marketing business where I will contract to market hospitality. I want something funky and fun to go with the name Pickle Pail

Industry/Entity Type

Marketing

Contact Information for Business Card

Marla Tennant-Greaves
Pickle Pail
Mobile: +61 2 407 392654
Email: marla@picklepail.com.au

Requirements
Must have
• Fun and modern
Should not have
• Not conservative

```html
<!DOCTYPE html>
<html lang="en">
<head>
<meta charset="utf-8">
<title>Pickle Pail Mobile – Business Card</title>
<link rel="stylesheet" href="https://fonts.googleapis.com/css2?family=Arimo:wght@400;700&display=swap">
<style>
  :root {
    --paper: #ffffff;
    --ink-blue: #0d2a8f;
    --accent-orange: #fbb416;
    --pattern-base: #f4f7f2;
    --ring-green: rgba(47, 194, 74, 0.85);
    --ring-deep-green: rgba(31, 107, 34, 0.8);
    --ring-red: rgba(216, 38, 15, 0.8);
    --ring-orange: rgba(243, 106, 28, 0.8);
    --ring-blue: rgba(42, 166, 224, 0.75);
    --ring-teal: rgba(63, 224, 160, 0.75);
    --brand-ink: #1b1b1b;
  }
  html, body {
    margin: 0;
    padding: 0;
    width: 1200px;
    height: 720px;
    overflow: hidden;
    background: var(--paper);
  }
  .card {
    position: relative;
    width: 1200px;
    height: 720px;
    background: var(--paper);
    font-family: "Arimo", Arial, sans-serif;
    overflow: hidden;
  }
  .card__art {
    position: absolute;
    left: 0;
    top: 0;
    width: 558px;
    height: 720px;
    background:
      radial-gradient(circle at 12% 10%, var(--ring-teal) 0, transparent 22%),
      radial-gradient(circle at 55% 8%, var(--ring-red) 0, transparent 24%),
      radial-gradient(circle at 95% 30%, var(--ring-orange) 0, transparent 26%),
      radial-gradient(circle at 4% 48%, var(--ring-blue) 0, transparent 20%),
      radial-gradient(circle at 25% 28%, var(--ring-deep-green) 0, transparent 22%),
      radial-gradient(circle at 15% 85%, var(--ring-green) 0, transparent 28%),
      radial-gradient(circle at 85% 82%, var(--ring-deep-green) 0, transparent 28%),
      radial-gradient(circle at 50% 95%, var(--ring-green) 0, transparent 22%),
      var(--pattern-base);
  }
  .card__divider {
    position: absolute;
    left: 558px;
    top: 0;
    width: 16px;
    height: 720px;
    background: var(--accent-orange);
  }
  .brand {
    position: absolute;
    left: 0;
    width: 558px;
    top: 322px;
    margin: 0;
    text-align: center;
    font-weight: 700;
    font-size: 38px;
    line-height: 46px;
    text-transform: uppercase;
    color: var(--brand-ink);
  }
  .contact__name {
    position: absolute;
    left: 623px;
    top: 117px;
    margin: 0;
    font-weight: 700;
    font-size: 44px;
    line-height: 50px;
    color: var(--ink-blue);
    white-space: nowrap;
  }
  .contact__details {
    position: absolute;
    right: 107px;
    top: 280px;
    margin: 0;
    text-align: right;
    font-size: 31px;
    line-height: 47px;
    color: var(--ink-blue);
    white-space: nowrap;
  }
</style>
</head>
<body>
  <main class="card">
    <div class="card__art" role="img" aria-label="Decorative pattern of interlocking green, red, orange and blue rings with a jar illustration"></div>
    <p class="brand">Pickle Pail<br>Mobile</p>

    <div class="card__divider"></div>

    <h1 class="contact__name">Marla Tennant-Greaves</h1>
    <p class="contact__details">
      Phone: 612-407-392654<br>
      Email: marla@picklepail.com.au
    </p>
  </main>
</body>
</html>
```